Business Card Design Project

Hi,

We are a new modern sheet metal business and I require a business card for our sales reps.

The card should be double sided and standout in a crowd.

I have attached our logo and our website is www.plyform.com.au.

Please ask if you have any further questions
Updates

hi everyone, 

I'm wondering if we can try to lighten the cards mood.  Everyone is using black and I'm not sure how that would be accepted in real life.

Gordon

Reason: Still No receiving what I was hoping for.

Industry/Entity Type

Business

Requirements
Must have
• double sided

```html
<!DOCTYPE html>
<html lang="en">
<head>
<meta charset="utf-8">
<title>Plyform Sheetmetal – Business Card</title>
<link rel="stylesheet" href="https://fonts.googleapis.com/css2?family=Arimo:wght@400;700&display=swap">
<style>
  :root {
    --brand-blue: #1f2b7e;
    --paper: #ffffff;
    --ink-grey: #77797f;
    --stage: #e6e7eb;
  }
  * { box-sizing: border-box; margin: 0; padding: 0; }
  html, body { width: 1200px; height: 846px; overflow: hidden; }
  body {
    background: var(--stage);
    font-family: "Arimo", Arial, sans-serif;
    position: relative;
  }
  .card {
    position: absolute;
    top: 269px;
    width: 540px;
    height: 308px;
    overflow: hidden;
    box-shadow: 0 6px 18px rgba(0,0,0,0.18);
  }
  .card--back { left: 40px; background: var(--brand-blue); }
  .card--front { left: 620px; background: var(--paper); }

  .wordmark {
    position: absolute; font-weight: 700; line-height: 0.95;
    text-transform: uppercase; white-space: nowrap;
  }
  .wordmark__name { display: block; font-size: 32px; letter-spacing: -0.5px; }
  .wordmark__trade { display: block; font-size: 14px; letter-spacing: 3.6px; margin-top: 5px; }
  .tagline { position: absolute; font-size: 9px; white-space: nowrap; }

  /* front */
  .front-band {
    position: absolute; left: 80px; top: 0; width: 196px; height: 100%;
    background: var(--brand-blue);
  }
  .card--front .wordmark { left: 94px; top: 82px; color: var(--paper); }
  .card--front .tagline { left: 95px; top: 146px; color: var(--paper); }

  .contact { position: absolute; left: 312px; top: 172px; color: var(--ink-grey); }
  .contact__address { font-size: 8.5px; line-height: 1.25; }
  .contact__line { font-size: 22px; line-height: 1.05; }
  .contact__label { color: var(--brand-blue); font-weight: 700; margin-right: 6px; }
  .contact__web { color: var(--brand-blue); font-weight: 700; font-size: 13px; letter-spacing: 0.5px; margin-top: 3px; }

  /* back */
  .back-panel {
    position: absolute; left: 296px; top: 110px; width: 196px; height: 198px;
    background: var(--paper);
  }
  .card--back .wordmark { left: 310px; top: 140px; color: var(--brand-blue); }
  .card--back .tagline { left: 311px; top: 204px; color: var(--brand-blue); }
  .back-web {
    position: absolute; left: 268px; top: 262px;
    transform: rotate(-90deg); transform-origin: left top;
    color: var(--paper); font-size: 11px; font-weight: 700; letter-spacing: 0.6px;
    line-height: 14px; white-space: nowrap;
  }
</style>
</head>
<body>
  <section class="card card--back" aria-label="Card back">
    <div class="back-panel"></div>
    <div class="back-web">www.plyform.com.au</div>
    <div class="wordmark">
      <span class="wordmark__name">Plyform</span>
      <span class="wordmark__trade">Sheetmetal</span>
    </div>
    <p class="tagline">Flashings | Gutter | Rainwater Goods</p>
  </section>

  <section class="card card--front" aria-label="Card front">
    <div class="front-band"></div>
    <div class="wordmark">
      <span class="wordmark__name">Plyform</span>
      <span class="wordmark__trade">Sheetmetal</span>
    </div>
    <p class="tagline">Flashings | Gutter | Rainwater Goods</p>
    <div class="contact">
      <p class="contact__address">22 Quarry Road Harlow Park Q 4300<br>PO Box 318 Harlow Park Q 4300</p>
      <p class="contact__line"><span class="contact__label">P</span>3555 0142</p>
      <p class="contact__line"><span class="contact__label">F</span>3555 0198</p>
      <p class="contact__web">www.plyform.com.au</p>
    </div>
  </section>
</body>
</html>
```